Mobile Spray Tan Business needs continuity for logo, website, biz cards etc.

I am starting a mobile spray tanning business. I would like all my components for my business to 'match'. The logo and design parameters to be the same on the website, my vehicle wrap, business cards etc. I would like some alternate logo graphics for multiple uses across multiple platforms (website, Facebook, twitter, blog). I have built a sample .biz website (glow-haven.biz) which will give some idea of what I'm looking for. I am not tied to the color purple for the logo or branding, but I am very attached to the caricature with the purple hair (I have purple hair). Another consideration is my vehicle is orange. Feel free to take liberties with color changes, just keep the girl with the purple hair. The vehicle will be wrapped on both sides and the rear (not the hood/bonnet or roof). I would like the vehicle wrap to include a scan code (or room for a scan code) that takes them to my website.
Updates

Hi everyone,

I want to thank you for submitting on this project.  I am a first time entrepreneur and I'm really hoping to make a great first impression.  Please feel free to ask any questions and I look forward to your submissions.

Sincerely,
Margaret

Industry/Entity Type

Business

```html
<!DOCTYPE html>
<html lang="en">
<head>
<meta charset="utf-8">
<title>Glow Haven – Mobile Spray Tan Banners</title>
<link rel="stylesheet" href="https://fonts.googleapis.com/css2?family=Syncopate:wght@700&family=Questrial&family=Crimson+Text:ital@1&display=swap">
<style>
  :root {
    --ink: #141414;
    --band: #1e1e1e;
    --gold: #c49a06;
    --white: #ffffff;
    --sky-light: #eaf6fd;
    --sky: #a9d3ee;
    --sky-deep: #7fb8e0;
    --lilac: #d9cdf0;
    --mint: #e3f4c8;
    --blush: #f7c9d8;
    --violet: #7a2fa8;
    --skin: #f3b48c;
  }
  * { margin: 0; padding: 0; box-sizing: border-box; }
  html, body { width: 1200px; height: 960px; overflow: hidden; background: var(--band); }
  .canvas { position: relative; width: 1200px; height: 960px; background: var(--band); }

  .banner { position: absolute; left: 0; width: 1200px; overflow: hidden; }
  .banner--light {
    top: 0; height: 444px;
    background:
      radial-gradient(ellipse at 20% 20%, var(--lilac) 0%, transparent 45%),
      radial-gradient(ellipse at 72% 18%, var(--mint) 0%, transparent 40%),
      radial-gradient(ellipse at 45% 95%, var(--blush) 0%, transparent 50%),
      var(--white);
  }
  .banner--sky {
    top: 478px; height: 448px;
    background:
      radial-gradient(ellipse at 50% 55%, var(--sky-light) 0%, transparent 55%),
      linear-gradient(180deg, var(--sky) 0%, var(--sky-deep) 100%);
  }

  .mascot {
    position: absolute;
    border-radius: 40% 40% 20% 20%;
    background: linear-gradient(180deg, var(--violet) 0%, var(--skin) 55%, var(--violet) 100%);
    opacity: 0.85;
  }
  .banner--light .mascot { left: 12px; top: 0; width: 258px; height: 396px; }
  .banner--sky .mascot { left: 846px; top: 32px; width: 264px; height: 384px; }

  .brand-name {
    position: absolute;
    font-family: "Syncopate", sans-serif;
    font-weight: 700;
    font-size: 78px;
    line-height: 1;
    color: var(--ink);
    white-space: nowrap;
    letter-spacing: 2px;
  }
  .banner--light .brand-name { left: 285px; top: 118px; }
  .banner--sky .brand-name { left: 40px; top: 104px; }

  .service {
    position: absolute;
    font-family: "Questrial", sans-serif;
    font-size: 52px;
    line-height: 1;
    color: var(--gold);
    white-space: nowrap;
    padding-bottom: 4px;
    border-bottom: 2px solid var(--gold);
  }
  .banner--light .service { left: 486px; top: 248px; }
  .banner--sky .service { left: 246px; top: 240px; }

  .tagline {
    position: absolute;
    font-family: "Crimson Text", serif;
    font-style: italic;
    font-size: 28px;
    line-height: 1;
    color: var(--ink);
    white-space: nowrap;
  }
  .banner--light .tagline { left: 450px; top: 316px; }
  .banner--sky .tagline { left: 214px; top: 312px; }
</style>
</head>
<body>
<main class="canvas">
  <section class="banner banner--light">
    <div class="mascot" role="img" aria-label="Illustration of a smiling woman with long purple hair holding a spray tan gun"></div>
    <h1 class="brand-name">GLOW HAVEN</h1>
    <p class="service">Mobile Spray tan</p>
    <p class="tagline">Stay Out Of the Sun , Just Don’t Look Like It</p>
  </section>

  <section class="banner banner--sky">
    <div class="mascot" role="img" aria-label="Illustration of a smiling woman with long purple hair holding a spray tan gun"></div>
    <h2 class="brand-name">GLOW HAVEN</h2>
    <p class="service">Mobile Spray tan</p>
    <p class="tagline">Stay Out Of the Sun , Just Don’t Look Like It</p>
  </section>
</main>
</body>
</html>
```